Outstanding but small benefit administration firm serving large clients needs a website redesign

While the content on our current website is fine, when people arrive at our website, they know immediately that it was designed years ago. We are looking for something that can potentially be maintained on a content management system because we would like to hire a google certified expert to help with adwords and they often want to change the website or add meta data. We want the design to be mobile device friendly.

As for our company, we stress data accuracy, client customization and outstanding customer service. All of our competitors are large corporations (TelvarPrine, Doltry, Quimby, PayloomCrest, etc.). When we get a client, they stay with us. So many of our competitors do a horrible job with administration that many companies just think that's the way it is in this industry. We need to change that thinking! There is someone who can do it right at a reasonable price. We have very few out of scope fees. KWT knows how to make the transition from one administrator to us as painless as possible.

We like our current colors. We don't have a lot of time to write additional content.

Target Market(s)

Companies with 5,000 to 50,000 employees

Coding

Coded - Design and coding required

Number of Pages Required

2 page

Font styles to use
Sans Serif

Requirements
Must have
• If everything doesn't fit on one page, please show me what the second page would look like. For example, if there are See More links, what happens?
• We need for people to be able to submit short contact us with their company name as a required field.
• Ideally this website will be put on wordpress or something similar.
• Must be mobile device friendly.
Should not have
• Login, Register, Maps of our location, website search

```html
<!DOCTYPE html>
<html lang="en">
<head>
<meta charset="utf-8">
<title>Keystone Welfare Trust</title>
<link href="https://fonts.googleapis.com/css2?family=Montserrat:wght@400;500;600&family=Arimo:wght@400&display=swap" rel="stylesheet">
<style>
  :root {
    --page-bg: #4e5560;
    --white: #ffffff;
    --navy: #2a2f8c;
    --nav-blue: #1f3399;
    --logo-grey: #7a7d80;
    --text-grey: #444a50;
    --panel: #e4e1d9;
    --footer: #d6dae2;
    --footer-line: #c3c8d1;
    --accent-green: #7bbf3a;
  }
  * { margin: 0; padding: 0; box-sizing: border-box; }
  html, body { width: 914px; height: 1200px; overflow: hidden; background: var(--page-bg); }
  .page {
    position: absolute; left: 49px; top: 0; width: 817px; height: 1200px;
    background: var(--white); font-family: "Arimo", Arial, sans-serif;
  }
  .site-header { position: absolute; left: 0; top: 0; width: 817px; height: 111px; border-bottom: 1.5px solid var(--nav-blue); }
  .brand { position: absolute; left: 20px; top: 45px; display: flex; align-items: center; gap: 8px; }
  .brand-dot { width: 10px; height: 10px; border-radius: 50%; background: var(--accent-green); }
  .brand-name { font-family: "Montserrat", sans-serif; font-weight: 400; font-size: 20px; color: var(--logo-grey); }
  .main-nav { position: absolute; top: 55px; left: 0; font-family: "Montserrat", sans-serif; font-weight: 500; font-size: 10.5px; color: var(--nav-blue); }
  .main-nav a { position: absolute; white-space: nowrap; text-decoration: none; color: inherit; }
  .hero {
    position: absolute; left: 0; top: 111px; width: 817px; height: 343px;
    background: radial-gradient(circle at 62% 50%, #ffffff 0 12%, #31b6e8 24%, #7fd7f2 45%, #2f7fc9 75%, #a9e3f5 100%);
  }
  .hero-title { position: absolute; left: 21px; top: 36px; font-family: "Montserrat", sans-serif; font-weight: 500; font-size: 26px; line-height: 30px; color: #000; }
  .hero-dots { position: absolute; left: 719px; top: 301px; display: flex; gap: 8px; }
  .hero-dots span { width: 12px; height: 12px; border-radius: 50%; border: 2px solid #0b1030; background: transparent; }
  .hero-dots span.active { background: #14206a; }
  .difference { position: absolute; left: 46px; top: 518px; width: 726px; height: 132px; background: var(--panel); border-radius: 8px; }
  .difference h2 { position: absolute; left: 21px; top: 44px; font-family: "Montserrat", sans-serif; font-weight: 600; font-size: 29px; color: var(--navy); letter-spacing: 0.3px; }
  .difference p { position: absolute; left: 328px; top: 26px; width: 370px; font-size: 10px; line-height: 17.6px; color: var(--text-grey); }
  .services { position: absolute; left: 0; top: 744px; width: 817px; }
  .service { position: absolute; width: 200px; text-align: center; }
  .service-photo { width: 164px; height: 164px; margin: 0 auto; border-radius: 50%; border: 3px solid #c2c9d2; }
  .service h3 { margin-top: 24px; font-family: "Montserrat", sans-serif; font-weight: 500; font-size: 12px; line-height: 16px; color: var(--navy); }
  .service p { margin-top: 10px; font-size: 8.6px; line-height: 15.6px; color: var(--text-grey); padding: 0 16px; }
  .site-footer { position: absolute; left: 0; top: 1114px; width: 817px; height: 86px; background: var(--footer); border-top: 2px solid var(--footer-line); }
  .footer-nav { position: absolute; left: 72px; top: 23px; font-family: "Montserrat", sans-serif; font-size: 8.5px; color: var(--text-grey); display: flex; gap: 14px; letter-spacing: 0.3px; }
  .copyright { position: absolute; left: 72px; top: 42px; font-family: "Montserrat", sans-serif; font-size: 7.5px; color: var(--text-grey); }
</style>
</head>
<body>
<div class="page">
  <header class="site-header">
    <div class="brand"><span class="brand-dot"></span><span class="brand-name">Keystone Welfare Trust</span></div>
    <nav class="main-nav">
      <a style="left:409px">WHY KWT</a>
      <a style="left:478px">SERVICES</a>
      <a style="left:548px">TECHNOLOGY</a>
      <a style="left:640px">CASE STUDIES</a>
      <a style="left:734px">CONTACT</a>
    </nav>
  </header>

  <section class="hero" role="img" aria-label="Hand touching a glowing blue digital interface ring of service icons">
    <h1 class="hero-title">CUSTOMER<br>SERVICE MODEL</h1>
    <div class="hero-dots"><span class="active"></span><span></span><span></span></div>
  </section>

  <section class="difference">
    <h2>OUR DIFFERENCE</h2>
    <p>The benefits outsourcing industry is going through challenging times. Clients are asked to limit the complexity of plans offered and restrict customization and flexibility of administrative protocols. There is a trend towards off-shoring of customer service centers and long lead times for required system changes.</p>
  </section>

  <section class="services">
    <article class="service" style="left:98px">
      <div class="service-photo" role="img" aria-label="Blue stethoscope resting on medical paperwork" style="background:radial-gradient(circle at 45% 45%, #2f6f98, #7d8a95 55%, #c9c6c0)"></div>
      <h3>Health and<br>Welfare Administration</h3>
      <p>Lorem ipsum dolor sit amet, consectetuer adipiscing elit, sed diam nonummy nibh euismod tincidunt ut laoreet dolore magna aliquam erat volutpat. Ut wisi enim ad</p>
    </article>
    <article class="service" style="left:358px">
      <div class="service-photo" role="img" aria-label="Colleagues meeting around a table in a bright office" style="background:radial-gradient(circle at 50% 55%, #8f8a86, #c9c3bb 60%, #e6e3de)"></div>
      <h3>Defined Benefit<br>Administration</h3>
      <p>Lorem ipsum dolor sit amet, consectetuer adipiscing elit, sed diam nonummy nibh euismod tincidunt ut laoreet dolore magna aliquam erat volutpat. Ut wisi enim ad</p>
    </article>
    <article class="service" style="left:616px">
      <div class="service-photo" role="img" aria-label="Hands reviewing financial documents with a pen" style="background:radial-gradient(circle at 50% 50%, #f4f2f3, #c7d3e6 60%, #8ea3c6)"></div>
      <h3>Benefit Consulting<br>Service</h3>
      <p>Lorem ipsum dolor sit amet, consectetuer adipiscing elit, sed diam nonummy nibh euismod tincidunt ut laoreet dolore magna aliquam erat volutpat. Ut wisi enim ad</p>
    </article>
  </section>

  <footer class="site-footer">
    <nav class="footer-nav"><span>HOME</span><span>ABOUT</span><span>CONTACT</span></nav>
    <p class="copyright">Copyright © 2016 &nbsp;Keystone Welfare Trust, Inc.</p>
  </footer>
</div>
</body>
</html>
```